Ballet Sponsorship Ad

I need to have an ad created where my commercial real estate firm has a sponsorship ad for a ballet recital. The ad should include similar company branding to other ads and include a photo of my daughter congratulating her on the recital. The ad size MUST be 8.5" wide by 5.5" tall and needs to be sent in JPG and PDF format to me.

The contact information to include in the ad is:
274 W. Tollbridge Orchard Rd
Brookmere, OR 97415
(555) 463-5082
www.holtbankerre.com
desmond@holtbankerre.com

Real Estate

Requirements
Must have
• Photo of my daughter
• Company logo
• "Congratulations Lydia Banker"
• Company contact information

```html
<!DOCTYPE html>
<html lang="en">
<head>
<meta charset="utf-8">
<title>Holt-Banker Real Estate – Recital Sponsorship Ad</title>
<link rel="stylesheet" href="https://fonts.googleapis.com/css2?family=EB+Garamond:wght@400;500&display=swap">
<style>
  :root {
    --backdrop: #0b0a09;
    --paper: #ffffff;
    --forest: #0b6b45;
    --photo-dark: #4d6260;
    --photo-mid: #8fa3a0;
    --photo-light: #d9dedd;
    --name-grey: #a8b0ab;
    --ink-green: #11603f;
  }
  * { margin: 0; padding: 0; box-sizing: border-box; }
  html, body {
    width: 1200px; height: 888px; overflow: hidden;
    background: var(--backdrop);
  }
  .ad {
    position: absolute;
    left: 91px; top: 88px;
    width: 1019px; height: 658px;
    background: var(--paper);
    overflow: hidden;
    font-family: "EB Garamond", Garamond, serif;
  }
  .recital-photo {
    position: absolute; left: 0; top: 0;
    width: 600px; height: 646px;
    background:
      linear-gradient(90deg, rgba(255,255,255,0) 55%, var(--paper) 100%),
      radial-gradient(ellipse at 50% 40%, var(--photo-light) 0%, var(--photo-mid) 45%, var(--photo-dark) 100%);
  }
  .green-sweep { position: absolute; left: 0; top: 0; width: 1019px; height: 646px; }
  .headline {
    position: absolute; right: 53px; top: 164px;
    text-align: right; color: var(--paper);
    font-size: 57px; font-weight: 400; letter-spacing: 2px; line-height: 1;
  }
  .honoree {
    position: absolute; right: 53px; top: 226px;
    text-align: right; color: var(--name-grey);
    font-size: 56px; font-weight: 400; letter-spacing: 2px; line-height: 1;
  }
  .brand {
    position: absolute; right: 53px; top: 420px;
    display: flex; align-items: center; gap: 16px;
  }
  .brand-mark {
    width: 44px; height: 44px; border-radius: 50%;
    background: var(--forest);
  }
  .brand-name {
    color: var(--ink-green); font-size: 50px; font-weight: 400; line-height: 1; white-space: nowrap;
  }
  .contact {
    position: absolute; right: 53px; top: 558px;
    text-align: right; color: var(--ink-green);
    font-size: 21px; line-height: 23px; font-style: normal;
  }
  .contact span + span { margin-left: 18px; }
  .footer-bar {
    position: absolute; left: 0; bottom: 0; width: 100%; height: 12px;
    background: var(--forest);
  }
</style>
</head>
<body>
  <div class="ad">
    <div class="recital-photo" role="img" aria-label="Photo of a young ballerina in a leotard and skirt, arms raised, standing at a tall window in a sunlit studio"></div>

    <svg class="green-sweep" viewBox="0 0 1019 646" aria-hidden="true">
      <defs>
        <linearGradient id="sweepFill" x1="0" y1="0" x2="1" y2="0">
          <stop offset="0" stop-color="#0b6b45" stop-opacity="0"/>
          <stop offset="0.35" stop-color="#0b6b45" stop-opacity="0.55"/>
          <stop offset="0.6" stop-color="#0b6b45" stop-opacity="1"/>
          <stop offset="1" stop-color="#0a6a44" stop-opacity="1"/>
        </linearGradient>
        <linearGradient id="sweepShade" x1="0" y1="0" x2="0" y2="1">
          <stop offset="0" stop-color="#034a2d" stop-opacity="0.9"/>
          <stop offset="1" stop-color="#034a2d" stop-opacity="0"/>
        </linearGradient>
      </defs>
      <path d="M300 0 L1019 0 L1019 338 C860 320 700 300 560 296 C380 292 160 360 0 420 L0 260 C120 180 220 90 300 0 Z" fill="url(#sweepFill)"/>
      <path d="M560 0 L1019 0 L1019 200 C900 140 760 80 560 0 Z" fill="url(#sweepShade)"/>
      <path d="M420 0 C620 90 820 160 1019 190" stroke="#ffffff" stroke-opacity="0.12" stroke-width="2" fill="none"/>
      <path d="M480 250 C640 150 820 80 1019 60" stroke="#ffffff" stroke-opacity="0.1" stroke-width="2" fill="none"/>
    </svg>

    <h1 class="headline">CONGRATULATIONS</h1>
    <p class="honoree">Lydia Banker</p>

    <div class="brand">
      <div class="brand-mark"></div>
      <div class="brand-name">Holt-Banker Real Estate</div>
    </div>

    <address class="contact">
      <div>274 W. Tollbridge Orchard Rd, Brookmere, OR 97415</div>
      <div><span>(555) 463-5082</span><span>www.holtbankerre.com</span><span>desmond@holtbankerre.com</span></div>
    </address>

    <div class="footer-bar"></div>
  </div>
</body>
</html>
```